Life Coaching and Career Coaching company needs new website with bold, modern, videos

We need a whole new website that is heavy on video. We are a small company who sells personal wellbeing services like career coaching, life coaching, and group coaching programs. The programs all help people design a better life.
FULL BRIEF ATTACHED and STYLE GUIDE
Also, look at https://www.pinevaultery.com/coaching and corvanly.com and https://www.tarnwick.life/ for a small amount of inspiration.

Industry/Entity Type

personal well-being/life coaching/career coaching

Number of Pages Required

3 page

Other font styles liked:
• fonts are in the brief

Requirements
Must have
• read the brief please - it's all in there. (things like the look, feel, how it will have lots of video, etc,)
Nice to have
• something really different looking and breakthrough. visually stunning. very trustworthy. Please read the brief, its all in there.
Should not have
• should not look like other life coaching websites. must have video!

```html
<!DOCTYPE html>
<html lang="en">
<head>
<meta charset="utf-8">
<title>Wayfold Living Project — Life &amp; Career Coaching</title>
<link href="https://fonts.googleapis.com/css2?family=Comfortaa:wght@400;600;700&family=Didact+Gothic&display=swap" rel="stylesheet">
<style>
:root{
  --coral:#f0605e;
  --ink:#2f2f33;
  --text:#3c3c40;
  --muted:#f3f3f3;
  --white:#ffffff;
  --plum:#420a3e;
  --star:#f5b400;
}
*{box-sizing:border-box;margin:0;padding:0}
html,body{width:1200px;height:3000px;overflow:hidden}
body{position:relative;background:var(--white);font-family:"Didact Gothic",sans-serif;color:var(--text)}
.abs{position:absolute}
.heading{font-family:"Comfortaa",sans-serif;color:var(--ink);font-weight:600}
.chevron{position:absolute;width:20px;height:26px}
.btn{position:absolute;display:flex;align-items:center;justify-content:center;background:var(--coral);color:var(--white);font-family:"Comfortaa",sans-serif;font-size:15px;font-weight:600;border-radius:6px}

/* header */
.site-header{top:0;left:0;width:1200px;height:84px;background:var(--white)}
.brand{left:111px;top:20px;color:#7a7a7e;font-size:30px;letter-spacing:1px;line-height:1}
.brand small{display:block;font-size:14px;text-align:right;letter-spacing:1px;margin-top:-2px}
.nav{left:480px;top:31px;display:flex;gap:34px;font-size:16px;color:var(--text)}
.search{left:1045px;top:21px;width:42px;height:42px;border-radius:50%;background:var(--coral)}

/* hero */
.hero{top:84px;left:0;width:1200px;height:601px;background:linear-gradient(90deg,#c9a47c 0%,#d8c6ae 22%,#d2dfe3 48%,#d4e2e6 70%,#e2d6d8 100%)}
.hero-photo{top:84px;left:0;width:600px;height:601px;background:radial-gradient(ellipse at 35% 55%,#d0a777 0%,#c59b76 35%,rgba(205,214,216,0) 75%)}
.play-hero{left:565px;top:349px;width:70px;height:70px}
.welcome{left:677px;top:243px;font-size:34px}
.hero-title{left:677px;top:300px;font-size:54px;font-weight:700;white-space:nowrap}
.hero-title span{color:var(--coral)}
.hero-copy{left:680px;top:390px;width:370px;font-size:16px;line-height:24px}

/* section titles */
.section-title{width:1200px;left:0;text-align:center;font-size:36px}

/* program cards */
.program-card{width:228px;height:189px;border-radius:12px;overflow:hidden}
.program-label{width:228px;text-align:center;font-family:"Comfortaa",sans-serif;font-size:21px;color:var(--ink)}
.play-ring{position:absolute;left:50%;top:50%;width:48px;height:48px;margin:-24px 0 0 -24px}

/* who we are */
.who-panel{top:1180px;left:0;width:623px;height:540px;background:var(--muted)}
.who-photo{top:1180px;left:623px;width:577px;height:540px;background:linear-gradient(135deg,#e4e6e8 0%,#d8dadb 45%,#e9e1d8 75%,#b89b78 100%)}
.who-title{left:111px;top:1260px;font-size:34px}
.who-copy{left:111px;top:1350px;width:458px;font-size:17px;line-height:25.7px;text-align:justify}

/* testimonials */
.testimonial{width:302px;height:298px;background:var(--white);box-shadow:0 4px 14px rgba(0,0,0,.06)}
.testimonial-photo{position:absolute;left:0;top:0;width:302px;height:199px}
.avatar{position:absolute;left:19px;top:225px;width:50px;height:50px;border-radius:50%;border:2px solid var(--coral)}
.t-name{position:absolute;left:83px;top:224px;font-size:17px;color:var(--ink)}
.t-stars{position:absolute;left:83px;top:251px;display:flex;gap:1px}
.arrow{width:28px;height:16px}

/* programs band */
.band{top:2308px;left:0;width:1200px;height:380px;background:linear-gradient(90deg,#ec6e6c 0%,#f07a77 50%,#ec6f6d 100%)}
.band-title{top:2372px;font-size:36px;color:var(--white)}
.band-copy{top:2456px;left:170px;width:860px;text-align:center;color:var(--white);font-size:16.5px;line-height:25.7px}
.btn-outline{left:539px;top:2584px;width:121px;height:52px;background:transparent;border:1.5px solid var(--white)}

/* footer */
.site-footer{top:2688px;left:0;width:1200px;height:312px;background:var(--plum)}
.footer-brand{left:111px;top:2784px;color:var(--white);font-size:44px;letter-spacing:1px;line-height:1}
.footer-brand small{display:block;font-size:20px;text-align:right;letter-spacing:1px}
.social{top:2873px;width:32px;height:32px;border-radius:50%;background:var(--white)}
.footer-col h4{font-family:"Comfortaa",sans-serif;font-weight:700;font-size:15px;color:var(--white);margin-bottom:14px}
.footer-col li{list-style:none;font-size:16px;color:var(--white);line-height:28.5px}
.copyright{top:2950px;left:0;width:1200px;text-align:center;color:var(--white);font-size:15px}
</style>
</head>
<body>

<header class="abs site-header">
  <div class="abs brand">WAYFOLD LIVING<small>PROJECT</small></div>
  <nav class="abs nav"><span>Home</span><span>Who we are</span><span>Programs</span><span>Testimonials</span><span>Contact us</span></nav>
  <div class="abs search">
    <svg width="42" height="42" viewBox="0 0 42 42"><circle cx="20" cy="20" r="5" fill="none" stroke="#fff" stroke-width="2"/><line x1="24" y1="24" x2="27" y2="27" stroke="#fff" stroke-width="2.4" stroke-linecap="round"/></svg>
  </div>
</header>

<section>
  <div class="abs hero"></div>
  <div class="abs hero-photo" role="img" aria-label="Woman with eyes closed breathing fresh air in warm sunlight"></div>
  <svg class="abs play-hero" viewBox="0 0 70 70"><circle cx="35" cy="35" r="34" fill="#f0605e" fill-opacity=".3"/><circle cx="35" cy="35" r="22" fill="#f0605e"/><path d="M31 28 L42 35 L31 42Z" fill="#fff"/></svg>
  <div class="abs heading welcome">Welcome to</div>
  <div class="abs heading hero-title">Wayfold <span>Living</span></div>
  <p class="abs hero-copy">Lorem ipsum dolor sit amet, consectetur adipiscing elit, sed do labore et dolore magna aliqua.</p>
  <div class="btn" style="left:680px;top:468px;width:120px;height:51px">Get started</div>
</section>

<section>
  <h2 class="abs heading section-title" style="top:760px">Types of Programs</h2>
  <svg class="chevron" style="left:590px;top:806px" viewBox="0 0 20 26"><path d="M4 3 L15 13 L4 23" fill="none" stroke="#f0605e" stroke-width="5" stroke-linejoin="round"/></svg>

  <div class="abs program-card" style="left:111px;top:864px;background:linear-gradient(135deg,#e8e6e3,#a58468 60%,#6f5340)" role="img" aria-label="Coach speaking to a seated group in a bright studio">
    <svg class="play-ring" viewBox="0 0 48 48"><circle cx="24" cy="24" r="21" fill="none" stroke="#fff" stroke-width="3"/><path d="M20 16 L32 24 L20 32Z" fill="#fff"/></svg></div>
  <div class="abs program-card" style="left:361px;top:864px;background:linear-gradient(135deg,#f0ebe4,#c9a486 55%,#8a6a55)" role="img" aria-label="Two women talking during a one-to-one session">
    <svg class="play-ring" viewBox="0 0 48 48"><circle cx="24" cy="24" r="21" fill="none" stroke="#fff" stroke-width="3"/><path d="M20 16 L32 24 L20 32Z" fill="#fff"/></svg></div>
  <div class="abs program-card" style="left:611px;top:864px;background:linear-gradient(135deg,#a86b55,#4f4a4a 55%,#2c3440)" role="img" aria-label="People sitting in a circle for a group session">
    <svg class="play-ring" viewBox="0 0 48 48"><circle cx="24" cy="24" r="21" fill="none" stroke="#fff" stroke-width="3"/><path d="M20 16 L32 24 L20 32Z" fill="#fff"/></svg></div>
  <div class="abs program-card" style="left:860px;top:864px;background:linear-gradient(135deg,#c69a78,#7a5440 55%,#3d2a22)" role="img" aria-label="Audience seated at a workshop">
    <svg class="play-ring" viewBox="0 0 48 48"><circle cx="24" cy="24" r="21" fill="none" stroke="#fff" stroke-width="3"/><path d="M20 16 L32 24 L20 32Z" fill="#fff"/></svg></div>

  <div class="abs program-label" style="left:111px;top:1070px">career coaching</div>
  <div class="abs program-label" style="left:361px;top:1070px">Life coaching</div>
  <div class="abs program-label" style="left:611px;top:1070px">Group coaching</div>
  <div class="abs program-label" style="left:860px;top:1070px">Dedicated coaching</div>
</section>

<section>
  <div class="abs who-panel"></div>
  <div class="abs who-photo" role="img" aria-label="Relaxed woman at a desk beside wooden letter blocks spelling wellness"></div>
  <h2 class="abs heading who-title">Who we are</h2>
  <svg class="chevron" style="left:111px;top:1303px" viewBox="0 0 20 26"><path d="M4 3 L15 13 L4 23" fill="none" stroke="#f0605e" stroke-width="5" stroke-linejoin="round"/></svg>
  <p class="abs who-copy">Lorem ipsum dolor sit amet, consectetur adipiscing elit, sed do eiusmod tempor incididunt ut labore et dolore magna aliqua. Ut enim ad minim veniam, quis nostrud exercitation ullamco laboris nisi ut aliquip ex ea commodo consequat. Duis aute irure dolor in reprehenderit in voluptate velit esse cillum dolore eu fugiat nulla pariatur. Excepteur sint occaecat cupidatat non proident, sunt in culpa qui officia deserunt mollit anim id est laborum.</p>
  <div class="btn" style="left:111px;top:1588px;width:120px;height:51px">Learn More</div>
</section>

<section>
  <h2 class="abs heading section-title" style="top:1795px">Our Testimonials</h2>
  <svg class="chevron" style="left:590px;top:1841px" viewBox="0 0 20 26"><path d="M4 3 L15 13 L4 23" fill="none" stroke="#f0605e" stroke-width="5" stroke-linejoin="round"/></svg>

  <svg class="abs arrow" style="left:60px;top:2039px" viewBox="0 0 28 16"><path d="M26 8 H3 M9 2 L3 8 L9 14" fill="none" stroke="#666" stroke-width="1.6"/></svg>
  <svg class="abs arrow" style="left:1116px;top:2039px" viewBox="0 0 28 16"><path d="M2 8 H25 M19 2 L25 8 L19 14" fill="none" stroke="#666" stroke-width="1.6"/></svg>

  <div class="abs testimonial" style="left:111px;top:1908px">
    <div class="testimonial-photo" style="background:linear-gradient(90deg,#b89478,#e7d6c6 55%,#a98f7a)" role="img" aria-label="Smiling teacher in a classroom"></div>
    <svg class="play-ring" style="top:99px" viewBox="0 0 48 48"><circle cx="24" cy="24" r="13" fill="none" stroke="#fff" stroke-width="2"/><path d="M21 19 L29 24 L21 29Z" fill="#fff"/></svg>
    <div class="avatar" style="background:#d8b79c" role="img" aria-label="Portrait of Mary Jane"></div>
    <div class="t-name">Mary Jane</div>
    <div class="t-stars"><svg width="66" height="12" viewBox="0 0 66 12"><g fill="#f5b400"><path id="s" d="M6 0 L7.6 4 L12 4.3 L8.6 7.1 L9.7 11.5 L6 9 L2.3 11.5 L3.4 7.1 L0 4.3 L4.4 4Z"/><use href="#s" x="13"/><use href="#s" x="26"/><use href="#s" x="39"/><use href="#s" x="52"/></g></svg></div>
  </div>

  <div class="abs testimonial" style="left:449px;top:1908px">
    <div class="testimonial-photo" style="background:linear-gradient(90deg,#8c8c88,#3f5f8a 50%,#c9c9c6)" role="img" aria-label="Smiling man in a denim shirt"></div>
    <svg class="play-ring" style="top:99px" viewBox="0 0 48 48"><circle cx="24" cy="24" r="13" fill="none" stroke="#fff" stroke-width="2"/><path d="M21 19 L29 24 L21 29Z" fill="#fff"/></svg>
    <div class="avatar" style="background:#6a7f9c" role="img" aria-label="Portrait of Smith"></div>
    <div class="t-name">Smith</div>
    <div class="t-stars"><svg width="66" height="12" viewBox="0 0 66 12"><g fill="#f5b400"><use href="#s"/><use href="#s" x="13"/><use href="#s" x="26"/><use href="#s" x="39"/><use href="#s" x="52"/></g></svg></div>
  </div>

  <div class="abs testimonial" style="left:786px;top:1908px">
    <div class="testimonial-photo" style="background:linear-gradient(90deg,#b6a08e,#e3d4c6 55%,#b8a690)" role="img" aria-label="Smiling teacher with pupils behind her"></div>
    <svg class="play-ring" style="top:99px" viewBox="0 0 48 48"><circle cx="24" cy="24" r="13" fill="none" stroke="#fff" stroke-width="2"/><path d="M21 19 L29 24 L21 29Z" fill="#fff"/></svg>
    <div class="avatar" style="background:#c9a58a" role="img" aria-label="Portrait of Jane"></div>
    <div class="t-name">Jane</div>
    <div class="t-stars"><svg width="66" height="12" viewBox="0 0 66 12"><g fill="#f5b400"><use href="#s"/><use href="#s" x="13"/><use href="#s" x="26"/><use href="#s" x="39"/><use href="#s" x="52"/></g></svg></div>
  </div>
</section>

<section>
  <div class="abs band" role="img" aria-label="Person raising arms in a sunlit field, tinted coral"></div>
  <h2 class="abs heading section-title band-title">our programs</h2>
  <svg class="chevron" style="left:590px;top:2413px" viewBox="0 0 20 26"><path d="M4 3 L15 13 L4 23" fill="none" stroke="#fff" stroke-width="5" stroke-linejoin="round"/></svg>
  <p class="abs band-copy">Lorem ipsum dolor sit amet, consectetur adipiscing elit, sed do eiusmod tempor incididunt ut labore et dolore magna aliqua. Ut enim ad minim veniam, quis nostrud exercitation ullamco laboris nisi ut aliquip ex ea commodo consequat. Duis aute irure dolor in reprehenderit in voluptate velit esse cillum dolore eu fugiat nulla pariatur. Excepteur sint occaecat cupidatat non proident, sunt in culpa qui officia deserunt mollit anim id est laborum.</p>
  <div class="btn btn-outline">Learn More</div>
</section>

<footer>
  <div class="abs site-footer"></div>
  <div class="abs footer-brand">WAYFOLD LIVING<small>PROJECT</small></div>
  <div class="abs social" style="left:167px" aria-label="Social link"></div>
  <div class="abs social" style="left:205px" aria-label="Social link"></div>
  <div class="abs footer-col" style="left:514px;top:2750px">
    <h4>QUICK LINKS</h4>
    <ul><li>Home</li><li>Who we are</li><li>Programs</li><li>Testimonials</li><li>Contact us</li></ul>
  </div>
  <div class="abs footer-col" style="left:701px;top:2750px">
    <h4>PROGRAMS</h4>
    <ul><li>Career coaching</li><li>Life coaching</li><li>Group coaching</li></ul>
  </div>
  <div class="abs footer-col" style="left:903px;top:2750px">
    <h4>OTHER LINKS</h4>
    <ul><li>Terms &amp; Conditions</li><li>Privacy Policy</li><li>About Us</li><li>Support</li></ul>
  </div>
  <div class="abs copyright">2024 Wayfold Living. All Rights Reserved.</div>
</footer>

</body>
</html>
```